Letterhead for louvre roof company in NZ

I require a letter head design for a company called Skyvane Group.
I would like a footer to the letter head and possibly a water mark.
See attached logo.

```html
<!DOCTYPE html>
<html lang="en">
<head>
<meta charset="utf-8">
<title>Skyvane Group Letterhead</title>
<link href="https://fonts.googleapis.com/css2?family=Source+Sans+3:wght@400;600;700&family=Arimo:wght@700&display=swap" rel="stylesheet">
<style>
  :root {
    --backdrop: #e3e4e4;
    --paper: #ffffff;
    --brand-orange: #f0801e;
    --watermark: #fbe3cb;
    --ink: #3b3b3b;
    --greeting-ink: #1a1f3a;
    --rule: #c9c9c9;
    --signature-tone: #d9d9d9;
  }
  * { box-sizing: border-box; margin: 0; padding: 0; }
  html, body { width: 1200px; height: 960px; overflow: hidden; }
  body {
    background: var(--backdrop);
    font-family: "Source Sans 3", "Myriad Pro", Arial, sans-serif;
    color: var(--ink);
  }
  .letterhead {
    position: absolute;
    left: 280px; top: 27px;
    width: 640px; height: 905px;
    background: var(--paper);
    overflow: hidden;
  }
  .header-band {
    position: absolute; top: 0; right: 0;
    width: 290px; height: 9px;
    background: var(--brand-orange);
    clip-path: polygon(12px 0, 100% 0, 100% 100%, 0 100%);
  }
  .sender {
    position: absolute; top: 26px; left: 380px;
    display: flex; gap: 10px;
    font-size: 8.5px; line-height: 1.3; color: #333;
  }
  .sender-address { padding-right: 10px; border-right: 1px solid var(--rule); }
  .sender-name { color: var(--brand-orange); font-weight: 700; }
  .sender-contact li { list-style: none; display: flex; align-items: center; gap: 4px; }
  .sender-contact svg { width: 7px; height: 7px; flex: none; }
  .brand {
    position: absolute; top: 66px; left: 60px;
    display: flex; align-items: center; gap: 8px;
  }
  .brand-square { width: 22px; height: 22px; background: var(--brand-orange); }
  .brand-name { font-size: 17px; font-weight: 700; color: var(--brand-orange); }
  .letter-body {
    position: absolute; top: 205px; left: 60px; width: 520px;
  }
  .greeting {
    font-family: "Arimo", Arial, sans-serif;
    font-weight: 700; font-size: 14px; color: var(--greeting-ink);
    margin-bottom: 14px;
  }
  .letter-body p {
    font-size: 12.5px; line-height: 1.3;
    margin-bottom: 18px; text-align: justify;
  }
  .signature {
    width: 130px; height: 48px; margin-top: 22px;
    background: linear-gradient(90deg, var(--signature-tone), #f2f2f2);
    border-radius: 4px;
  }
  .watermark {
    position: absolute; right: 30px; bottom: 110px;
    font-size: 64px; font-weight: 700; line-height: 1;
    color: var(--watermark);
    text-align: right;
  }
</style>
</head>
<body>
  <main class="letterhead">
    <div class="header-band"></div>

    <header class="sender">
      <div class="sender-address">
        <div class="sender-name">Skyvane Group</div>
        <div>PO Box 412, Harbour Road,</div>
        <div>Tidewater, 0610</div>
      </div>
      <ul class="sender-contact">
        <li><svg viewBox="0 0 10 10"><circle cx="5" cy="5" r="4.5" fill="var(--brand-orange)"/></svg>(021) 555 0148</li>
        <li><svg viewBox="0 0 10 10"><rect x="0.5" y="2" width="9" height="6" fill="var(--brand-orange)"/></svg>hello@skyvanegroup.co</li>
        <li><svg viewBox="0 0 10 10"><circle cx="5" cy="5" r="4.5" fill="var(--brand-orange)"/></svg>www.skyvanegroup.co</li>
      </ul>
    </header>

    <div class="brand">
      <span class="brand-square"></span>
      <span class="brand-name">Skyvane Group</span>
    </div>

    <section class="letter-body">
      <h1 class="greeting">Dear Mr. Hallam,</h1>
      <p>Lorem Ipsum is simply dummy text of the printing and typesetting industry. Lorem Ipsum has been the industry's standard dummy text ever since the 1500s, when an unknown printer took a galley of type and scrambled it to make a type specimen book. It has survived not only five centuries, but also the leap into electronic typesetting, remaining essentially unchanged.</p>
      <p>The standard chunk of Lorem Ipsum used since the 1500s is reproduced below for those interested. Sections 1.10.32 and 1.10.33 from "de Finibus Bonorum et Malorum" by Aurelan are also reproduced in their exact original form, accompanied by English versions from the 1914 translation by H.Marlow</p>
      <p>Lorem Ipsum is simply dummy text of the printing and typesetting industry. Lorem Ipsum has been the industry's standard dummy text ever since the 1500s, when an unknown printer took a galley of type and scrambled it to make a type specimen book. It has survived not only five centuries, but also the leap into electronic typesetting, remaining essentially unchanged. It was popularised in the</p>
      <p>The standard chunk of Lorem Ipsum used since the 1500s is reproduced below for those interested. Sections 1.10.32 and 1.10.33 from "de Finibus Bonorum et Malorum" by Aurelan are also reproduced in their exact original form, accompanied by English versions from the 1914 translation by H.Marlow</p>
      <div class="signature" role="img" aria-label="Handwritten signature of the sender"></div>
    </section>

    <div class="watermark" aria-hidden="true">Skyvane<br>Group</div>
  </main>
</body>
</html>
```